Business Card Design Project - IT Company

Kestrafield Information Technology Solutions
We are an Information Technology Company. We provide computer services to commercial companies. We would like a new card full color front and back with bleeding edge.
We have a logo that you can use or if you want to come up with a new logo that is fine too.
Our colors are mostly Maroon and black but be creative.
Sample Information
Brent R Okafor
4812 W Saguaro Ridge Drive
Suite 410
Tempe, AZ 85284
O: 602.914.2037
C: 602.468.1290
24/7: 888.914.2037
bokafor@kestrafield.example
www.kestrafield.example
Target Market(s)
Business of all sizes
Industry/Entity Type
Computer
Requirements
Must have
- Bleeding edge
full color on both sides

```html
<!DOCTYPE html>
<html lang="en">
<head>
<meta charset="utf-8">
<title>Kestrafield Business Card</title>
<link rel="stylesheet" href="https://fonts.googleapis.com/css2?family=Marcellus&family=PT+Serif:wght@400;700&display=swap">
<style>
  :root {
    --page: #ffffff;
    --maroon-red: #c8262b;
    --band-black: #231f20;
    --white: #ffffff;
    --text-grey: #6b6b6b;
    --card-border: #b9b9b9;
    --back-fill: #ffffff;
  }
  html, body {
    margin: 0;
    padding: 0;
    width: 1017px;
    height: 1200px;
    overflow: hidden;
    background: var(--page);
  }
  .canvas {
    position: relative;
    width: 1017px;
    height: 1200px;
  }
  .card {
    position: absolute;
    left: 83px;
    width: 852px;
    box-sizing: border-box;
    overflow: hidden;
  }
  .card--front {
    top: 70px;
    height: 499px;
    background: var(--maroon-red);
  }
  .card--back {
    top: 622px;
    height: 505px;
    background: var(--back-fill);
    border: 2px solid var(--card-border);
  }
  .brand {
    position: absolute;
    left: 0;
    right: 0;
    top: 190px;
    text-align: center;
    color: var(--white);
  }
  .brand__name {
    display: block;
    font-family: "Marcellus", serif;
    font-size: 66px;
    letter-spacing: 10px;
    line-height: 1;
    margin-left: 10px;
  }
  .brand__tagline {
    display: block;
    margin-top: 14px;
    font-family: "Marcellus", serif;
    font-size: 30px;
    letter-spacing: 0.5px;
  }
  .website {
    position: absolute;
    right: 38px;
    top: 445px;
    color: var(--white);
    font-family: "PT Serif", serif;
    font-size: 22px;
    line-height: 26px;
    letter-spacing: 3px;
  }
  .band {
    position: absolute;
    left: 0;
    right: 0;
    bottom: 0;
    height: 25px;
    background: var(--band-black);
  }
  .contact {
    position: absolute;
    left: 184px;
    top: 110px;
    font-family: "PT Serif", serif;
    color: var(--text-grey);
  }
  .contact__name {
    margin: 0 0 31px;
    font-size: 23px;
    font-weight: 700;
    letter-spacing: 2px;
    color: var(--maroon-red);
  }
  .contact__lines {
    margin: 0;
    font-style: normal;
    font-size: 25px;
    line-height: 31px;
    letter-spacing: 2px;
  }
  .contact__label {
    color: var(--maroon-red);
  }
</style>
</head>
<body>
<div class="canvas">
  <section class="card card--front">
    <div class="brand">
      <span class="brand__name">KESTRAFIELD</span>
      <span class="brand__tagline">Information Technology Solutions</span>
    </div>
    <div class="website">www.kestrafield.example</div>
    <div class="band"></div>
  </section>

  <section class="card card--back">
    <div class="contact">
      <h1 class="contact__name">Brent R Okafor</h1>
      <address class="contact__lines">
        4812 W Saguaro Ridge Drive<br>
        Suite 410<br>
        Tempe, AZ 85284<br>
        <span class="contact__label">O</span> 602.914.2037<br>
        <span class="contact__label">C</span> 602.468.1290<br>
        24/7: 888.914.2037<br>
        bokafor@kestrafield.example
      </address>
    </div>
  </section>
</div>
</body>
</html>
```